Merrow Sailcraft Works President Business Card Carbon fiber catamarans

Hi.. I need a new business card design.. I am the President of a high tech yacht builder. We build Carbon Fiber go fast catamarans... Maybe we use the file I am sharing to you as the back of the card.. We need to look cool and crisp ...

Target Market(s)

Affluent People who will purchase a cool yacht

Industry/Entity Type

Custom Yacht Builder

Contact Information for Business Card

Dale Penwarty , President, 517.608.2391 USA

Font styles to use
Serif

Requirements
Must have
• the clean crisp cool feel
Nice to have
• clean and crisp
Should not have
• Bold ugly

```html
<!DOCTYPE html>
<html lang="en">
<head>
<meta charset="utf-8">
<title>Merrow Sailcraft Works – Business Card</title>
<link href="https://fonts.googleapis.com/css2?family=Roboto:wght@400;500;700&display=swap" rel="stylesheet">
<style>
  :root {
    --stage: #2b2b2d;
    --carbon: #141416;
    --carbon-edge: #1f1f22;
    --paper: #f1f1f2;
    --ink: #151515;
    --silver: #c9cacd;
    --silver-soft: #9c9ea3;
  }
  * { margin: 0; padding: 0; box-sizing: border-box; }
  html, body {
    width: 1200px; height: 874px; overflow: hidden;
    background: var(--stage);
    font-family: 'Roboto', Arial, sans-serif;
  }
  .stage {
    width: 1200px; height: 874px;
    display: flex; flex-direction: column; align-items: center; justify-content: center;
    gap: 36px;
  }
  .card {
    position: relative;
    width: 640px; height: 366px;
    overflow: hidden;
    box-shadow: 0 14px 30px rgba(0,0,0,.45);
  }
  /* back side */
  .card-back {
    background: radial-gradient(ellipse at 45% 45%, var(--carbon-edge), var(--carbon) 75%);
    display: flex; align-items: center; justify-content: center;
  }
  .brand-lockup { display: flex; align-items: center; gap: 18px; }
  .brand-mark {
    width: 46px; height: 46px; border-radius: 50%;
    border: 3px solid var(--silver);
  }
  .brand-name {
    color: var(--silver);
    font-weight: 500; font-size: 30px;
    letter-spacing: 5px; text-transform: uppercase;
    line-height: 1.15;
  }
  /* front side */
  .card-front { background: var(--paper); }
  .card-front .carbon-panel { position: absolute; inset: 0; }
  .holder { position: absolute; left: 44px; top: 44px; color: var(--ink); }
  .holder-name { font-weight: 700; font-size: 21px; letter-spacing: .5px; text-transform: uppercase; }
  .holder-title { font-weight: 500; font-size: 12.5px; margin-top: 3px; }
  .contact { position: absolute; left: 44px; top: 176px; color: var(--ink); font-size: 14.5px; line-height: 1.35; }
  .address { margin-bottom: 8px; padding-left: 20px; }
  .contact-list { list-style: none; }
  .contact-list li { display: flex; align-items: center; gap: 8px; }
  .contact-list svg { width: 12px; height: 12px; fill: var(--ink); flex: none; }
  .front-brand {
    position: absolute; right: 40px; top: 50%; transform: translateY(-50%);
    width: 210px; display: flex; flex-direction: column; align-items: center; gap: 14px;
  }
  .front-brand .brand-mark { width: 120px; height: 120px; border-width: 5px; }
  .front-brand .brand-name { font-size: 15px; letter-spacing: 3px; text-align: center; }
</style>
</head>
<body>
<main class="stage">

  <section class="card card-back" aria-label="Card back">
    <div class="brand-lockup">
      <span class="brand-mark"></span>
      <span class="brand-name">Merrow<br>Sailcraft Works</span>
    </div>
  </section>

  <section class="card card-front" aria-label="Card front">
    <svg class="carbon-panel" viewBox="0 0 640 366" preserveAspectRatio="none" role="img" aria-label="Dark carbon fibre texture panel">
      <defs>
        <linearGradient id="carbonShade" x1="0" y1="0" x2="1" y2="1">
          <stop offset="0" stop-color="#1f1f22"/>
          <stop offset="1" stop-color="#121214"/>
        </linearGradient>
      </defs>
      <polygon points="370,0 640,0 640,366 290,366" fill="url(#carbonShade)"/>
    </svg>

    <div class="holder">
      <p class="holder-name">Dale Penwarty</p>
      <p class="holder-title">President</p>
    </div>

    <div class="contact">
      <p class="address">214 Harbor Reach Road<br>Newport, Rhode Island 02840</p>
      <ul class="contact-list">
        <li><svg viewBox="0 0 12 12"><path d="M2.5 1l2 2-1 1.3c.7 1.5 1.8 2.6 3.2 3.2L8 6.5l2 2L8.8 10.6C5 10 2 7 1.4 3.2z"/></svg>517-608-2391</li>
        <li><svg viewBox="0 0 12 12"><path d="M3 0h6v12H3zM4 1.5v8h4v-8z"/></svg>517-608-2394</li>
        <li><svg viewBox="0 0 12 12"><path d="M3 1h6v3H3zM1 5h10v5H9v2H3v-2H1zM4 8v3h4V8z"/></svg>517-608-2397</li>
        <li><svg viewBox="0 0 12 12"><path d="M0 2h12v8H0zM1 3l5 3.5L11 3v-.2H1z"/></svg>name@merrowsailcraft.com</li>
        <li><svg viewBox="0 0 12 12"><circle cx="6" cy="6" r="5.5"/></svg>www.merrowsailcraft.com</li>
      </ul>
    </div>

    <div class="front-brand">
      <span class="brand-mark"></span>
      <span class="brand-name">Merrow Sailcraft Works</span>
    </div>
  </section>

</main>
</body>
</html>
```